Business card design needed for rebranded top-end landscaping business

We need a new business card design, incorporating our logo (colours Green #8dc63f and Grey #8a8c8e) and also some options that include the colour dark navy (eg #000040) as our uniforms are navy with white and grey trim.

We are an innovative landscaping company that maintains high-end gardens for meticulous clients. We pride ourselves on our customer service, our professionalism, and our workmanship.

Our business name needs to be easily read and our branding needs to be bold and memorable, without screaming "tradesman"! We prefer clean lines over lots of fine detail.

The design MUST include:
- Business name ("Brambleton Gardenworks")
- Logo (file uploaded)
- Employee name
- Phone number
- Email address
- www.brambletongardenworks.com.au
- Facebook & Instagram logos
- The Turfcraft Guild logo (file uploaded) along with the word "Member"
- Licence "Lic. 618392K"

OPTIONAL inclusions:
- "Creating outdoor spaces for our community to be inspired, refreshed and re-energised"
- "Landscape Maintenance - Irrigation - Arboriculture" (dashes can be replaced with dots or other)
- "Fully qualified, licensed & insured"
- "Residential - Strata - Commercial - Real Estate" (dashes can be replaced with dots or other)

High-end professionals and retirees, real estate agents

Landscaping

See Project description

Sans Serif

Designer to choose colors to be used in the design.

• Must incorporate our logo, and colours Green #8dc63f and Grey #8a8c8e) from the logo, and the colour DARK NAVY (eg #000040).
• The design MUST include:
• - Business name ("Brambleton Gardenworks")
• - Logo (file uploaded)
• - Employee name
• - Phone number
• - Email address
• - www.brambletongardenworks.com.au
• - Facebook & Instagram logos
• - The Turfcraft Guild logo (file uploaded) along with the word "Member"
• - Licence "Lic. 618392K"
• OPTIONAL inclusions:
• - "Creating outdoor spaces for our community to be inspired, refreshed and re-energised"
• - "Landscape Maintenance - Irrigation - Arboriculture" (dashes can be replaced with dots or other)
• - "Fully qualified, licensed & insured"
• - "Residential - Strata - Commercial - Real Estate" (dashes can be replaced with dots or other)

```html
<!DOCTYPE html>
<html lang="en">
<head>
<meta charset="utf-8">
<title>Brambleton Gardenworks – Business Card</title>
<link href="https://fonts.googleapis.com/css2?family=Lato:wght@400;700;900&display=swap" rel="stylesheet">
<style>
  :root {
    --backdrop: #2e2e30;
    --card: #131313;
    --green: #8dc63f;
    --grey: #8a8c8e;
    --light: #c9cacb;
  }
  * { margin: 0; padding: 0; box-sizing: border-box; }
  html, body {
    width: 1200px; height: 900px; overflow: hidden;
    background: var(--backdrop);
    font-family: "Lato", Arial, sans-serif;
  }
  .card {
    position: absolute; left: 280px;
    width: 640px; height: 390px;
    background: var(--card);
    border-bottom: 12px solid var(--green);
    color: var(--light);
  }
  .card--front { top: 45px; }
  .card--back { top: 465px; }

  /* Front */
  .front-brand {
    position: absolute; top: 70px; left: 0; right: 0;
    text-align: center;
  }
  .brand-dot {
    display: block; margin: 0 auto 18px;
    width: 64px; height: 64px; border-radius: 50%;
    background: var(--grey);
  }
  .brand-name {
    font-weight: 700; color: var(--green);
    font-size: 38px; line-height: 1.05; letter-spacing: 0.5px;
  }
  .taglines {
    position: absolute; top: 262px; left: 0; right: 0;
    text-align: center; font-size: 19px; line-height: 1.55;
    color: var(--light);
  }
  .sep {
    display: inline-block; width: 8px; height: 8px; border-radius: 50%;
    background: var(--green); margin: 0 8px; vertical-align: middle;
  }

  /* Back */
  .social { position: absolute; top: 40px; left: 44px; display: flex; gap: 8px; }
  .social span {
    width: 20px; height: 20px; border-radius: 50%;
    border: 1.5px solid var(--grey);
  }
  .licence { position: absolute; top: 74px; left: 44px; font-size: 17px; color: var(--grey); }

  .back-brand {
    position: absolute; top: 120px; right: 44px;
    font-weight: 700; color: var(--green);
    font-size: 30px; line-height: 1.1; text-align: right;
  }

  .person {
    position: absolute; top: 190px; left: 44px;
    font-weight: 900; font-size: 22px; letter-spacing: 1px;
    color: var(--grey); text-transform: uppercase;
  }
  .person .surname { color: var(--green); }

  .contact { position: absolute; top: 236px; left: 44px; list-style: none; }
  .contact li {
    display: flex; align-items: center; gap: 8px;
    font-size: 17px; line-height: 26px; color: var(--light);
  }
  .contact svg { width: 15px; height: 15px; fill: var(--green); flex: none; }

  .membership {
    position: absolute; right: 64px; bottom: 34px;
    width: 150px; text-align: center;
  }
  .membership-label {
    font-weight: 700; font-size: 16px; color: var(--green);
    letter-spacing: 0.5px; margin-bottom: 8px;
  }
  .membership-badge {
    width: 140px; height: 76px; margin: 0 auto;
    background: #3a3a3c; border-radius: 4px;
  }
</style>
</head>
<body>

<section class="card card--front">
  <div class="front-brand">
    <span class="brand-dot"></span>
    <div class="brand-name">Brambleton<br>Gardenworks</div>
  </div>
  <div class="taglines">
    <p>Fully qualified<span class="sep"></span>Licensed &amp; insured</p>
    <p>Residential<span class="sep"></span>Strata<span class="sep"></span>Commercial<span class="sep"></span>Real Estate</p>
  </div>
</section>

<section class="card card--back">
  <div class="social" aria-label="Social media">
    <span></span><span></span>
  </div>
  <p class="licence">Lic. 618392K</p>

  <div class="back-brand">Brambleton<br>Gardenworks</div>

  <p class="person">Marcus <span class="surname">Hale</span></p>

  <ul class="contact">
    <li>
      <svg viewBox="0 0 16 16" aria-hidden="true"><path d="M3.5 1.5l2.5 0 1 3.5-1.8 1.3a9 9 0 0 0 4.5 4.5l1.3-1.8 3.5 1v2.5a1.5 1.5 0 0 1-1.5 1.5A12.5 12.5 0 0 1 2 3a1.5 1.5 0 0 1 1.5-1.5z"/></svg>
      044-987 654 321
    </li>
    <li>
      <svg viewBox="0 0 16 16" aria-hidden="true"><path d="M1 3h14v10H1z M2 4.2v.6l6 4 6-4v-.6z" fill-rule="evenodd"/></svg>
      info@brambletonmail.com
    </li>
    <li>
      <svg viewBox="0 0 16 16" aria-hidden="true"><circle cx="8" cy="8" r="7"/><path d="M1 8h14M8 1c-3 3.5-3 10.5 0 14M8 1c3 3.5 3 10.5 0 14" stroke="#131313" stroke-width="1.2" fill="none"/></svg>
      www.brambletongardenworks.com.au
    </li>
  </ul>

  <div class="membership">
    <p class="membership-label">MEMBER</p>
    <div class="membership-badge" role="img" aria-label="The Turfcraft Guild membership badge"></div>
  </div>
</section>

</body>
</html>
```